NEW Escape Room. Fun, Dark and Mysterious.

Escape Room Website. Bookings and scheduling of appointments will be organised with Bookvane through the site. Most appointments will be created online through the booking system with some payments coming through in person by drop-ins. Groups will be from 2 - 8 people with a sliding scale of prices. We will start with one game playable and one saying coming soon. We will also eventually have 4 games up and running at once so will need it to be able to expand. We don't have any images of the rooms because it all relies heavily on mystery. Appointments are each 1 hour long with 30 minutes in between.

Target Market(s)

15-35 year olds

Coding

Coded - Design and coding required

Number of Pages Required

5+ page

Font styles to use
Decorative

Colors

Designer to choose colors to be used in the design.

Requirements
Must have
• Graphics showing what an escape room is.
• Page for About - What is an escape room
• Page for Games - Showing each of the different games which can be played with links to booking page. We have one game to start - the surgeons shadows. A victorian doctors office and serial killers. Then a game coming soon which is aztec/mayan/jungle/harold Crane feel.
• FAQ Page
Nice to have
• Graphics for multiple players ie 2 players, 3 players, 4 players etc
• Dark and Mysterious feel.
• Inspiration from Puzzle Vault, Cipher Lodge, Quest Lockbox
Should not have
• Cartoony/childish. Pink.
• Not bloody or dripping letters etc - not cliche.
• Not horror themed.

```html
<!DOCTYPE html>
<html lang="en">
<head>
<meta charset="utf-8">
<title>Lantern Gate – Escape Room</title>
<link href="https://fonts.googleapis.com/css2?family=Exo+2:wght@400;500;700;800&family=Russo+One&display=swap" rel="stylesheet">
<style>
:root{
  --nav-bg:#06121a;
  --gold:#fdb000;
  --gold-text:#d9a514;
  --white:#ffffff;
  --hero-dark:#16263a;
  --hero-mid:#2c4560;
  --hero-glow:#b9c7cf;
  --section-bg:#1a120c;
  --footer-bg:#000000;
  --rule:#2e2e2e;
  --ring:#6d6d6d;
}
*{margin:0;padding:0;box-sizing:border-box}
html,body{width:1200px;height:1102px;overflow:hidden;background:var(--footer-bg)}
body{font-family:"Exo 2",sans-serif;color:var(--white);position:relative}
a{color:inherit;text-decoration:none}

.site-header{position:absolute;top:0;left:0;width:1200px;height:66px;background:var(--nav-bg);z-index:3}
.main-nav a{position:absolute;top:24px;font-size:12px;font-weight:700;letter-spacing:.2px}
.main-nav .active{color:var(--gold)}
.phone{position:absolute;left:793px;top:24px;display:flex;align-items:center;gap:7px;font-size:13px;font-weight:700}
.btn{position:absolute;display:flex;align-items:center;justify-content:center;font-weight:700;font-size:13px;color:#1a1a1a;background:var(--gold)}
.header-book{left:922px;top:16px;width:127px;height:34px}

.brand{position:absolute;left:520px;top:62px;width:160px;z-index:4;display:flex;flex-direction:column;align-items:center;gap:8px}
.brand-dot{width:46px;height:46px;border-radius:50%;background:var(--gold)}
.brand-name{font-size:18px;font-weight:700;color:var(--gold)}

.hero{position:absolute;top:66px;left:0;width:1200px;height:490px;
  background:radial-gradient(ellipse 120px 330px at 600px 230px,var(--hero-glow) 0%,#6d8799 45%,transparent 100%),
  linear-gradient(90deg,var(--hero-dark),var(--hero-mid) 30%,var(--hero-mid) 70%,var(--hero-dark))}
.hero-text{position:absolute;left:0;width:1200px;text-align:center}
.hero-welcome{top:138px;font-size:20px;font-weight:500;color:#4d4f52}
.hero-sub{top:164px;font-size:29px;font-weight:700;color:#3a3b3d}
.hero-title{top:206px;font-size:78px;font-weight:800;color:var(--gold-text);letter-spacing:-1px}
.hero-rooms{left:466px;top:377px;width:126px;height:34px;background:#1c1a16;border:2px solid var(--gold);color:var(--gold)}
.hero-book{left:607px;top:377px;width:127px;height:34px}

.who{position:absolute;top:556px;left:0;width:1200px;height:387px;
  background:radial-gradient(ellipse at 50% 40%,#2a1d12,var(--section-bg) 70%,#0d0906)}
.who-title{position:absolute;top:56px;width:1200px;text-align:center;font-family:"Russo One",sans-serif;font-size:24px}
.player{position:absolute;top:122px;width:150px;text-align:center}
.player-photo{width:150px;height:150px;border-radius:50%;border:4px solid var(--ring)}
.player-label{margin-top:11px;font-size:14px;font-weight:500}
.family{left:224px}.family .player-photo{background:linear-gradient(160deg,#c9d6c8,#6f8fa8 60%,#d8d4cc)}
.corporate{left:525px}.corporate .player-photo{background:linear-gradient(160deg,#d9d9d9,#5a6a86 55%,#e4e4e4)}
.friends{left:824px}.friends .player-photo{background:linear-gradient(180deg,#c7ccd1,#8d8f90 50%,#3b3b3b)}

.site-footer{position:absolute;top:943px;left:0;width:1200px;height:159px;background:var(--footer-bg);border-top:1px solid var(--gold)}
.social{position:absolute;top:33px;left:549px;display:flex;gap:9px}
.social span{width:17px;height:17px;border-radius:50%;background:var(--white)}
.footer-nav{position:absolute;top:75px;width:1200px;display:flex;justify-content:center;gap:17px;font-size:12px;font-weight:700}
.legal{position:absolute;top:118px;left:0;width:1200px;height:41px;border-top:1px solid var(--rule);font-size:10px}
.copyright{position:absolute;left:187px;top:13px}
.legal-links{position:absolute;left:865px;top:14px;display:flex;gap:12px}
</style>
</head>
<body>
<header class="site-header">
  <nav class="main-nav">
    <a class="active" href="#" style="left:149px">HOME</a>
    <a href="#" style="left:224px">ABOUT US</a>
    <a href="#" style="left:322px">GAMES</a>
    <a href="#" style="left:404px">CONTACT US</a>
    <a href="#" style="left:514px">FAQ</a>
  </nav>
  <div class="phone">
    <svg width="13" height="13" viewBox="0 0 24 24" fill="none" stroke="#fff" stroke-width="2"><path d="M22 16.9v3a2 2 0 0 1-2.2 2 19.8 19.8 0 0 1-8.6-3.1 19.5 19.5 0 0 1-6-6A19.8 19.8 0 0 1 2.1 4.2 2 2 0 0 1 4.1 2h3a2 2 0 0 1 2 1.7c.1 1 .4 1.9.7 2.8a2 2 0 0 1-.5 2.1L8 9.9a16 16 0 0 0 6 6l1.3-1.3a2 2 0 0 1 2.1-.4c.9.3 1.8.6 2.8.7a2 2 0 0 1 1.7 2z"/></svg>
    <span>000-000-000</span>
  </div>
  <a class="btn header-book" href="#">BOOK NOW</a>
</header>

<div class="brand">
  <span class="brand-dot"></span>
  <span class="brand-name">Lantern Gate</span>
</div>

<section class="hero" role="img" aria-label="Old carved wooden double doors opening onto misty light">
  <p class="hero-text hero-welcome">Welcome to</p>
  <p class="hero-text hero-sub">Escape Room</p>
  <h1 class="hero-text hero-title">Lantern Gate</h1>
  <a class="btn hero-rooms" href="#">VIEW ROOMS</a>
  <a class="btn hero-book" href="#">BOOK NOW</a>
</section>

<section class="who" aria-label="Who can play">
  <h2 class="who-title">WHO CAN PLAY</h2>
  <div class="player family">
    <div class="player-photo" role="img" aria-label="Family of three walking outdoors"></div>
    <p class="player-label">Family</p>
  </div>
  <div class="player corporate">
    <div class="player-photo" role="img" aria-label="Colleagues gathered around a laptop"></div>
    <p class="player-label">Corporate</p>
  </div>
  <div class="player friends">
    <div class="player-photo" role="img" aria-label="Group of friends walking together"></div>
    <p class="player-label">Friends</p>
  </div>
</section>

<footer class="site-footer">
  <div class="social"><span></span><span></span><span></span><span></span></div>
  <nav class="footer-nav">
    <a href="#">HOME</a><span>|</span>
    <a href="#">ABOUT US</a><span>|</span>
    <a href="#">GAMES</a><span>|</span>
    <a href="#">CONTACT US</a><span>|</span>
    <a href="#">FAQ</a>
  </nav>
  <div class="legal">
    <p class="copyright">Copyright © 2020 Lantern Gate. &nbsp;&nbsp; All Rights Reserved.</p>
    <p class="legal-links"><a href="#">Terms of Use</a><span>|</span><a href="#">Privacy Policy</a></p>
  </div>
</footer>
</body>
</html>
```